StaffNest banner and eDM design

We need banner ads and an eDM header to promote StaffNest.com.au (not currently live but logo and site design complete).

Banners should ideally be in flash with back-up gifs but we would be open to just animated gifs as well.

Banner sizes to be delivered are:
300x250
729x90
468x60
160x600

Best to keep banner file size under 25kb if possible (based on standard publisher specs)

For the eDM header, it should be around:
600 wide x
150-200 high

The advertising role is to promote the websites services which are related to making HR easy for small business owners - specifically relating to recruitment, induction, engagement and employee exit. I'll attach more details on this.
Updates

Target Market(s)

Small and medium business owners - slightly male skew

Industry/Entity Type

Small Business

Requirements
Must have
• Must match the look and feel and colour palette of the logo and website design that will be attached to this brief.

Must look professional

Must follow the copy guide for the frames as outlined in the attachment - there are 2 options for frame 3 listed. I'd like to get 2 sets of banners developed to cover both options.

Must have clear call-to-action
Nice to have
• Nice to have sophisticated animation if possible

I've added two potential images that could be used - either could be used to illustrate the 'Save time and improve results' line -
one focused on finding the right person
one is focused on improving results through a team

You could potentially use a screen grab of the site homepage in the design too - but only if eligible since none of the copy on it is finalised.

```html
<!DOCTYPE html>
<html lang="en">
<head>
<meta charset="utf-8">
<title>StaffNest – Save Time and Improve Results</title>
<link rel="stylesheet" href="https://fonts.googleapis.com/css2?family=Arimo:wght@400;700&display=swap">
<style>
  :root {
    --white: #ffffff;
    --blue-light: #2a7fd0;
    --blue-dark: #0c56a6;
    --swoosh: #dfe2e7;
    --swoosh-shade: #c3c8d0;
    --navy: #1b3f86;
    --red-top: #f04a44;
    --red-bottom: #c81d1a;
    --red-edge: #a91512;
    --chevron-disc: #3a1210;
    --team-tone: rgba(70, 190, 200, 0.55);
    --team-tone-soft: rgba(200, 205, 210, 0.45);
    --photo-tone-1: rgba(60, 60, 70, 0.55);
    --photo-tone-2: rgba(215, 205, 200, 0.5);
  }
  html, body {
    margin: 0;
    padding: 0;
    overflow: hidden;
    background: var(--white);
  }
  .banner {
    position: relative;
    width: 1200px;
    height: 148px;
    overflow: hidden;
    background: var(--white);
    font-family: "Arimo", Arial, sans-serif;
  }
  .banner__backdrop {
    position: absolute;
    inset: 0;
  }
  .banner__team-art {
    position: absolute;
    left: 0;
    top: 0;
    width: 250px;
    height: 148px;
    background:
      radial-gradient(ellipse 55% 70% at 28% 55%, var(--team-tone-soft) 0%, rgba(255,255,255,0) 100%),
      radial-gradient(ellipse 45% 55% at 62% 70%, var(--team-tone) 0%, rgba(255,255,255,0) 100%);
  }
  .banner__photo {
    position: absolute;
    left: 270px;
    top: 0;
    width: 250px;
    height: 148px;
    background:
      radial-gradient(ellipse 30% 55% at 52% 75%, var(--photo-tone-1) 0%, rgba(255,255,255,0) 100%),
      radial-gradient(ellipse 45% 60% at 45% 40%, var(--photo-tone-2) 0%, rgba(255,255,255,0) 100%);
  }
  .banner__headline {
    position: absolute;
    left: 500px;
    top: 0;
    width: 430px;
    height: 148px;
    display: flex;
    align-items: center;
    justify-content: center;
    margin: 0;
    color: var(--white);
    font-size: 27px;
    font-weight: 700;
    line-height: 1.4;
    text-align: center;
  }
  .banner__brand {
    position: absolute;
    left: 948px;
    top: 12px;
    display: flex;
    align-items: center;
    gap: 8px;
    color: var(--navy);
    font-size: 30px;
    font-weight: 700;
    letter-spacing: -0.5px;
  }
  .banner__brand-dot {
    width: 26px;
    height: 26px;
    border-radius: 50%;
    background: var(--navy);
  }
  .banner__cta {
    position: absolute;
    left: 940px;
    top: 76px;
    width: 248px;
    height: 62px;
    box-sizing: border-box;
    border: 1px solid var(--red-edge);
    border-radius: 7px;
    background: linear-gradient(180deg, var(--red-top) 0%, var(--red-bottom) 100%);
    display: flex;
    align-items: center;
    padding-left: 20px;
    color: var(--white);
    font-size: 21px;
    font-weight: 700;
    text-decoration: none;
  }
  .banner__cta-icon {
    position: absolute;
    right: 10px;
    top: 10px;
    width: 42px;
    height: 42px;
  }
</style>
</head>
<body>
  <div class="banner">
    <svg class="banner__backdrop" width="1200" height="148" viewBox="0 0 1200 148" aria-hidden="true">
      <defs>
        <linearGradient id="bandGradient" x1="0" y1="0" x2="1" y2="1">
          <stop offset="0" stop-color="var(--blue-light)"/>
          <stop offset="1" stop-color="var(--blue-dark)"/>
        </linearGradient>
        <linearGradient id="swooshGradient" x1="0" y1="0" x2="0" y2="1">
          <stop offset="0" stop-color="var(--swoosh-shade)"/>
          <stop offset="1" stop-color="var(--swoosh)"/>
        </linearGradient>
      </defs>
      <path d="M236,0 L254,0 C268,45 276,95 280,148 L262,148 C258,95 250,45 236,0 Z" fill="url(#swooshGradient)"/>
      <path d="M515,0 C482,45 470,100 476,148 L930,148 L930,0 Z" fill="url(#bandGradient)"/>
    </svg>

    <div class="banner__team-art" role="img" aria-label="Illustration of a team pulling a rope along a rising arrow"></div>
    <div class="banner__photo" role="img" aria-label="Photo of a cheering businesswoman at her laptop"></div>

    <h1 class="banner__headline">Save Time and Improve<br>Results...</h1>

    <div class="banner__brand">
      <span class="banner__brand-dot"></span>
      <span class="banner__brand-name">StaffNest</span>
    </div>

    <a class="banner__cta" href="#">
      Find Out More
      <svg class="banner__cta-icon" viewBox="0 0 42 42" aria-hidden="true">
        <circle cx="21" cy="21" r="20" fill="var(--chevron-disc)"/>
        <path d="M13,12 L21,21 L13,30" fill="none" stroke="var(--red-top)" stroke-width="5" stroke-linecap="round" stroke-linejoin="round"/>
        <path d="M22,12 L30,21 L22,30" fill="none" stroke="var(--red-top)" stroke-width="5" stroke-linecap="round" stroke-linejoin="round"/>
      </svg>
    </a>
  </div>
</body>
</html>
```